Vodka Bottle Label - Lune Vodka

I need a bottle label for a vodka I'd like to make called Lune Vodka.
I would like a label that looks elegant and fresh. I would like some mountains and colours to be red and white. Open to other colours being added but not too colourful. "Lune" means fresh, dawn in polish, i would like if mountains or something extra was added to the label too. I would like the Lune Vodka name not to be too small.
The vodka is made in australia and is 37%.

I would love to have a little bit of gold colour in the label!

I will provide the back label words when completing my decision.

i'd like to make it more simple and less european looking. More australian.

I saw a bottle like this and i did like the concept.

https://www.oakbarrelcellars.com.au/spirits/grey-vodka-range?srsltid=XqTz81mwkPLd04-hr-q7w93nfbzkgd_mR2yTpaMWxJeQ6vcbTnZsLpo

Target Market(s)

Vodka Drinkers

Industry/Entity Type

Alcohol

Colors
EB3D1F
EC4F4E
F09395
F8D3D4
FCEDEE

Requirements
Must have
• red and white colours incorporated, mountains or freshness on it.
Nice to have
• Fresh and clean look. Classy

```html
<!DOCTYPE html>
<html lang="en">
<head>
<meta charset="utf-8">
<title>Lune Vodka – Bottle Label</title>
<link rel="stylesheet" href="https://fonts.googleapis.com/css2?family=Montserrat:wght@300;500;600;700&display=swap">
<style>
  :root {
    --backdrop: #e6e9ed;
    --label-white: #ffffff;
    --label-blush: #fcedee;
    --red: #eb3d1f;
    --red-soft: #ec4f4e;
    --pink: #f09395;
    --pink-pale: #f8d3d4;
    --gold: #c9a24a;
    --ink: #5a2a26;
  }
  * { margin: 0; padding: 0; box-sizing: border-box; }
  html, body {
    width: 953px;
    height: 1200px;
    overflow: hidden;
    background: var(--backdrop);
  }
  .canvas {
    position: relative;
    width: 953px;
    height: 1200px;
    font-family: "Montserrat", sans-serif;
  }
  .neck-band {
    position: absolute;
    left: 326px;
    top: 40px;
    width: 300px;
    height: 130px;
    background: var(--red);
    border: 3px solid var(--gold);
    border-radius: 6px;
    display: flex;
    align-items: center;
    justify-content: center;
  }
  .neck-name {
    font-weight: 700;
    font-size: 52px;
    letter-spacing: 2px;
    color: var(--label-white);
  }
  .front-label {
    position: absolute;
    left: 96px;
    top: 220px;
    width: 761px;
    height: 930px;
    background: radial-gradient(ellipse at 50% 35%, var(--label-white) 0%, var(--label-blush) 80%);
    border: 3px solid var(--gold);
    border-radius: 4px;
    overflow: hidden;
  }
  .badge {
    position: absolute;
    left: 50%;
    top: 120px;
    width: 440px;
    height: 638px;
    transform: translateX(-50%);
  }
  .badge-line {
    fill: none;
    stroke: var(--gold);
    stroke-width: 3;
  }
  .badge-text { font-family: "Montserrat", sans-serif; }
  .badge-premium { font-size: 26px; font-weight: 600; letter-spacing: 9px; fill: var(--gold); }
  .badge-name { font-size: 100px; font-weight: 700; fill: var(--red); }
  .badge-kind { font-size: 46px; font-weight: 600; letter-spacing: 3px; fill: var(--red-soft); }
  .badge-process { font-size: 24px; font-weight: 600; letter-spacing: 2px; fill: var(--gold); }
  .mountain-scene {
    position: absolute;
    left: 0;
    right: 0;
    top: 790px;
    height: 70px;
    background: linear-gradient(180deg, var(--pink-pale) 0%, var(--pink) 100%);
  }
  .volume {
    position: absolute;
    left: 34px;
    bottom: 22px;
    font-size: 30px;
    font-weight: 300;
    letter-spacing: 2px;
    color: var(--ink);
  }
  .strength {
    position: absolute;
    right: 36px;
    bottom: 24px;
    font-size: 28px;
    font-weight: 300;
    letter-spacing: 1px;
    color: var(--ink);
  }
  .strength small {
    font-size: 15px;
    letter-spacing: 1px;
  }
</style>
</head>
<body>
<main class="canvas">
  <div class="neck-band">
    <span class="neck-name">LUNE</span>
  </div>

  <section class="front-label">
    <svg class="badge" viewBox="-200 -290 400 580" aria-label="Lune Vodka badge">
      <defs>
        <path id="arc-top" d="M -150 -205 Q 0 -262 150 -205"/>
        <path id="arc-bottom" d="M -160 208 Q 0 262 160 208"/>
      </defs>
      <rect class="badge-line" x="-190" y="-275" width="380" height="550" rx="95"/>
      <rect class="badge-line" x="-160" y="-175" width="320" height="350" rx="26"/>
      <line class="badge-line" x1="-160" y1="-150" x2="-188" y2="-185"/>
      <line class="badge-line" x1="160" y1="-150" x2="188" y2="-185"/>
      <line class="badge-line" x1="-160" y1="150" x2="-188" y2="185"/>
      <line class="badge-line" x1="160" y1="150" x2="188" y2="185"/>
      <line class="badge-line" x1="-160" y1="45" x2="160" y2="45"/>

      <text class="badge-text badge-premium" text-anchor="middle">
        <textPath href="#arc-top" startOffset="50%">PREMIUM</textPath>
      </text>
      <text class="badge-text badge-name" x="0" y="25" text-anchor="middle" textLength="280" lengthAdjust="spacingAndGlyphs">LUNE</text>
      <text class="badge-text badge-kind" x="0" y="118" text-anchor="middle">VODKA</text>
      <text class="badge-text badge-process" text-anchor="middle">
        <textPath href="#arc-bottom" startOffset="50%">CHARCOAL FILTERED</textPath>
      </text>
    </svg>

    <div class="mountain-scene" role="img" aria-label="Mountain range at dawn in soft red and pink"></div>

    <span class="volume">1L</span>
    <span class="strength">37% <small>ALC/VOL</small></span>
  </section>
</main>
</body>
</html>
```